I want to revise my business card design and get a more modern and up to date design.

Brolvane Handyman Sevices originated from a family-owned and operated contractor business, performing home renovation, addition, and construction work in the NYC area since 2004. Today, we specialize in reliable and affordable handyman services for residential and commercial clients In 2014, we expanded to northern New Jersey. In 2016, we brought quality home improvement and repair services to new Bucks County, PA, and nearby New Jersey areas.
Target Market(s)
Home owners and business that might be looking for a General contractor, handyman, cleaning services and Home maintenance and property.
Industry/Entity Type
Construction Company
Contact Information for Business Card
I am open to new ideas
Colors
Designer to choose colors to be used in the design.
Look and feel
Each slider illustrates characteristics of the customer's brand and the style your logo design should communicate.

```html
<!DOCTYPE html>
<html lang="en">
<head>
<meta charset="utf-8">
<title>Brolvane Handyman Sevices – Business Cards</title>
<link rel="stylesheet" href="https://fonts.googleapis.com/css2?family=Oswald:wght@400;600&family=Open+Sans:wght@700&display=swap">
<style>
  :root {
    --red: #e10613;
    --black: #111111;
    --white: #ffffff;
    --backdrop: #e9e9e9;
    --ink: #1a1a1a;
  }
  * { margin: 0; padding: 0; box-sizing: border-box; }
  html, body { width: 1200px; height: 956px; overflow: hidden; }
  body {
    background: var(--backdrop);
    position: relative;
    font-family: "Oswald", sans-serif;
  }
  .card {
    position: absolute;
    width: 560px;
    height: 320px;
    background: var(--white);
    overflow: hidden;
    box-shadow: 0 6px 18px rgba(0,0,0,0.12);
  }
  /* Front */
  .card--front { left: 70px; top: 100px; }
  .front__band { position: absolute; left: 0; width: 100%; background: var(--red); }
  .front__band--top { top: 0; height: 70px; border-bottom: 6px solid var(--black); }
  .front__band--bottom { bottom: 0; height: 88px; border-top: 6px solid var(--black); }
  .brand {
    position: absolute;
    left: 0; right: 0; top: 76px; bottom: 94px;
    display: flex; align-items: center; justify-content: center; gap: 16px;
  }
  .brand__dot { width: 44px; height: 44px; border-radius: 50%; background: var(--red); flex: none; }
  .brand__name {
    font-family: "Open Sans", sans-serif;
    font-weight: 700;
    font-size: 34px;
    color: var(--black);
    letter-spacing: -0.5px;
  }
  /* Back */
  .card--back { left: 570px; top: 500px; }
  .back__emblem {
    position: absolute; left: 34px; top: 110px;
    display: flex; flex-direction: column; align-items: center; gap: 12px;
    width: 150px;
  }
  .back__emblem .brand__dot { width: 110px; height: 110px; }
  .back__emblem .brand__name { font-size: 17px; text-align: center; line-height: 1.2; }
  .back__contact {
    position: absolute; right: 0; top: 0;
    width: 360px; height: 145px;
    background: var(--red);
    color: var(--white);
    padding: 40px 30px 0 34px;
  }
  .contact__name { font-weight: 600; font-size: 22px; letter-spacing: 0.5px; text-transform: uppercase; margin-bottom: 8px; }
  .contact__line { display: flex; align-items: center; gap: 8px; font-size: 15px; font-weight: 400; line-height: 1.55; }
  .contact__icon { width: 15px; height: 15px; flex: none; }
  .back__services {
    position: absolute; right: 0; top: 145px;
    width: 360px; height: 70px;
    padding: 8px 30px 0 34px;
    color: var(--ink);
    font-size: 15px; line-height: 1.3;
  }
  .back__accent {
    position: absolute; right: 0; bottom: 0;
    width: 255px; height: 105px;
    background: var(--red);
  }
</style>
</head>
<body>

<section class="card card--front" aria-label="Card front">
  <div class="front__band front__band--top"></div>
  <div class="brand">
    <span class="brand__dot"></span>
    <span class="brand__name">Brolvane Handyman Sevices</span>
  </div>
  <div class="front__band front__band--bottom"></div>
</section>

<section class="card card--back" aria-label="Card back">
  <div class="back__emblem">
    <span class="brand__dot"></span>
    <span class="brand__name">Brolvane Handyman Sevices</span>
  </div>

  <div class="back__contact">
    <p class="contact__name">Teodoro Valmont</p>
    <p class="contact__line">
      <svg class="contact__icon" viewBox="0 0 16 16" aria-hidden="true">
        <circle cx="8" cy="8" r="8" fill="#fff"/>
        <path d="M5.6 4.2l1.3 1.6-.7 1c.5 1.1 1.3 1.9 2.4 2.4l1-.7 1.6 1.3-.8 1.3c-2.8-.4-5-2.6-5.4-5.4z" fill="#e10613"/>
      </svg>
      (215) 555-0142
    </p>
    <p class="contact__line">
      <svg class="contact__icon" viewBox="0 0 16 16" aria-hidden="true">
        <circle cx="8" cy="8" r="8" fill="#fff"/>
        <rect x="3.8" y="5" width="8.4" height="6" fill="none" stroke="#e10613" stroke-width="1.2"/>
        <path d="M3.8 5l4.2 3.4L12.2 5" fill="none" stroke="#e10613" stroke-width="1.2"/>
      </svg>
      brolvanehandyman@mail.com
    </p>
  </div>

  <div class="back__services">
    <p>Commercial and Residential Contractor</p>
    <p>Handyman | Technician | Repair</p>
    <p>Improve | Maintain | Remodel</p>
  </div>

  <div class="back__accent"></div>
</section>

</body>
</html>
```